Cover Design Project for Book About Data and Opinion/Political Polling

Need a cover for a paperback book (and possibly ebook) about data and research, specifically public opinion polling.

The book is titled "Harbor of Echoes" and the subtitle is "How Lighthouse Keepers Charted the Northern Coast". It focuses on two core themes - the drivers behind why political polls are no longer reliable, and what it would take to fix that.

Something that screams "data" or "information", appeals to consumers of public opinion polls, and is colorful with a fair amount of red and blue, would be ideal. Preferably something graphical that implies worsening quality

Its 6x9 trim and at 229 pages has a spine of approximately 0.516". Including bleed, the dimensions needed are roughly 12.77"x9.25"

The lower left corner of the back cover should be free of content so the barcode can be placed there.

Some content attached.

Target Market(s)

Consumers of opinion polls
Pollsters/Polling Organizations
High-Net Worth Individuals

Font styles to use
Serif

Colors
0355a3
ec1f27

Requirements
Must have
• Red and Blue colors
• Imagery that tells potential readers the contents are data-oriented but consumable by people regardless of their data/tech literacy
Nice to have
• More color than just red and blue
Should not have
• Any sort of political partisanship
• The long bio on the back cover (use the short one, the long one was only provided for context)

```html
<!DOCTYPE html>
<html lang="en">
<head>
<meta charset="utf-8">
<title>Harbor of Echoes – Book Cover</title>
<link rel="stylesheet" href="https://fonts.googleapis.com/css2?family=Fredoka:wght@500;600;700&display=swap">
<style>
  :root {
    --cover-blue: #0b55a3;
    --cover-red: #e4222b;
    --spine-edge: #0a3f7a;
    --accent-sky: #2a9ee3;
    --text-light: #ffffff;
    --page-bg: #ffffff;
    --frame-line: #333333;
  }
  * { margin: 0; padding: 0; box-sizing: border-box; }
  html, body {
    width: 1200px; height: 874px; overflow: hidden;
    background: var(--page-bg);
  }
  body { font-family: "Fredoka", "Trebuchet MS", sans-serif; color: var(--text-light); }
  .canvas {
    position: relative; width: 1200px; height: 874px;
    border: 1px solid var(--frame-line);
  }
  .book-wrap {
    position: absolute; left: 48px; top: 46px;
    width: 1103px; height: 781px;
    background: var(--cover-blue);
    border: 1px solid var(--spine-edge);
    overflow: hidden;
  }
  .back-red-panel { position: absolute; left: 0; top: 0; }

  /* Back cover */
  .author-photo {
    position: absolute; left: 56px; top: 136px;
    width: 147px; height: 193px;
    background: linear-gradient(160deg, #8a5a44 0%, #5b3b30 45%, #27324a 100%);
  }
  .author-bio {
    position: absolute; left: 220px; top: 139px; width: 258px;
    font-size: 12.4px; font-weight: 600; line-height: 15.9px;
  }
  .author-credentials {
    position: absolute; left: 56px; top: 350px;
    font-size: 14.5px; font-weight: 600; line-height: 18px;
  }

  /* Spine */
  .spine {
    position: absolute; left: 519px; top: 0; width: 64px; height: 100%;
    border-left: 2px solid var(--spine-edge);
    border-right: 2px solid var(--spine-edge);
  }
  .spine-title {
    position: absolute; left: 50%; top: 133px;
    transform-origin: 0 0;
    transform: rotate(90deg) translate(0, -50%);
    white-space: nowrap;
    font-size: 44px; font-weight: 600; line-height: 1;
  }
  .spine-author {
    position: absolute; left: 50%; top: 594px;
    transform-origin: 0 0;
    transform: rotate(-90deg) translate(-122px, -50%);
    white-space: nowrap; line-height: 1.05;
  }
  .spine-author .label { display: block; font-size: 9px; font-weight: 500; }
  .spine-author .name { display: block; font-size: 13px; font-weight: 600; }

  /* Front cover */
  .front-title {
    position: absolute; left: 583px; width: 520px; top: 124px;
    text-align: center; font-size: 54px; font-weight: 600; line-height: 1;
  }
  .front-art {
    position: absolute; left: 679px; top: 227px;
    width: 328px; height: 326px;
    background: linear-gradient(135deg, #1fa39a 0%, #1f8fb8 40%, #e8474f 65%, #1c9a8a 100%);
  }
  .front-subtitle {
    position: absolute; left: 663px; top: 596px; width: 370px;
    font-size: 29px; font-weight: 600; line-height: 38px;
  }
  .subtitle-mark {
    position: absolute; left: 1023px; top: 582px;
    font-size: 88px; font-weight: 700; line-height: 1;
    color: var(--accent-sky);
  }
</style>
</head>
<body>
<div class="canvas">
  <div class="book-wrap">
    <svg class="back-red-panel" width="520" height="520" viewBox="0 0 520 520" aria-hidden="true">
      <polygon points="0,0 520,0 520,420 0,510" fill="var(--cover-red)"/>
    </svg>

    <section class="back-cover">
      <div class="author-photo" role="img" aria-label="Portrait photo of the author"></div>
      <p class="author-bio">Short Author Bio:<br>Daniel Marsh holds a BA and MA in Political Science from Ridgeview University and has conducted research for multiple advocacy groups, synthesizing the findings into reports cited by national news outlets as well as being used to make policy. He continues to provide his expertise on data and research as a consultant while building his company.</p>
      <p class="author-credentials">Daniel Marsh holds<br>BA and MA in Political Science<br>Ridgeview University</p>
    </section>

    <section class="spine">
      <h2 class="spine-title">Harbor of Echoes</h2>
      <div class="spine-author"><span class="label">Author</span><span class="name">Daniel Marsh holds</span></div>
    </section>

    <section class="front-cover">
      <h1 class="front-title">Harbor of Echoes</h1>
      <div class="front-art" role="img" aria-label="Four-panel illustration of hands casting ballots, opinion poll box, a tablet with data form and a laptop showing research"></div>
      <p class="front-subtitle">How Lighthouse Keepers Charted the Northern Coast</p>
      <span class="subtitle-mark" aria-hidden="true">?</span>
    </section>
  </div>
</div>
</body>
</html>
```